Display board and Flyer Design

We are advertising our business in the local travel centre. We have a package where we get a lightbox (A1 - 594 x 841) and brochure display (either 2 x A4 or 4xDL). We would like to advertise Thornfield Lodge 1852 utilising the design for the gin label attached (minus the gin of course). We would also like to bring attention to the fact that the shop Ashcombe Herbals Co is also at Thornfield Lodge as well as Garden and Gallery and gin tasting. For the brochure we are aiming to advertise everything we do at Thornfield Lodge, we would like the front to be the same as the above for the display board and the back similar to the Ashcombe Herbals brochure that is also attached (essentially so the brochure could sit either way in the display stands. We would then like the internal pages of the brochure to highlight the garden, gallery, giftshop and gin tasting. I have attached another brochure that was designed for our wholesale market. I would like the brochure to have a similar look and feel as the Ashcombe Herbals Co brochure utilising panama and helvetica nue fonts where able Once we have a basic design we can provide some more photography for specific elements i.e. Gin, gallery, giftshop, garden

Font styles to use
Other font styles liked:
• panama/ helvetica

Requirements
Must have
• similar feel to existing ashcombe herbals co brochure
Nice to have
• similar fonts panama/helvetica nue
Should not have
• a design that is nothing like what our brand already is

```html
<!DOCTYPE html>
<html lang="en">
<head>
<meta charset="utf-8">
<title>Thornfield Lodge 1852 – Display Board</title>
<link rel="stylesheet" href="https://fonts.googleapis.com/css2?family=Alfa+Slab+One&family=Bebas+Neue&family=Roboto+Condensed:wght@700&display=swap">
<style>
  :root {
    --sheet-bg: #f2efe9;
    --wall-light: #8d8170;
    --wall-mid: #6f6455;
    --wall-dark: #4a4238;
    --garden-light: #6e6b5c;
    --garden-dark: #3f3d33;
    --house-light: #a29684;
    --house-mid: #7c7262;
    --leaf-tone: #e4ddd0;
    --leaf-soft: #ece7dd;
    --ink-light: #ffffff;
  }
  * { margin: 0; padding: 0; box-sizing: border-box; }
  html, body {
    width: 1200px; height: 1102px; overflow: hidden;
    background: var(--sheet-bg);
  }
  .sheet { position: relative; width: 1200px; height: 1102px; }

  .poster {
    position: absolute; left: 59px; top: 75px;
    width: 668px; height: 945px; overflow: hidden;
  }
  .poster__collage, .poster__title {
    position: absolute; left: 0; top: 0; width: 668px; height: 945px;
  }
  .title-numerals { font-family: "Bebas Neue", sans-serif; fill: var(--ink-light); }
  .title-slab { font-family: "Alfa Slab One", serif; fill: var(--ink-light); }
  .poster__caption {
    position: absolute; left: 0; right: 0; top: 838px;
    text-align: center;
    font-family: "Roboto Condensed", "Helvetica Neue", sans-serif;
    font-weight: 700; font-size: 15.5px; line-height: 21px;
    color: var(--ink-light);
  }

  .botanical {
    position: absolute; left: 787px; top: 78px;
    width: 413px; height: 536px;
    background:
      radial-gradient(ellipse 60% 55% at 58% 48%, var(--leaf-tone) 0%, var(--leaf-soft) 70%, var(--sheet-bg) 100%);
  }
</style>
</head>
<body>
<main class="sheet">
  <section class="poster">
    <svg class="poster__collage" viewBox="0 0 668 945">
      <defs>
        <linearGradient id="wallTone" x1="0" y1="0" x2="1" y2="1">
          <stop offset="0" stop-color="var(--wall-light)"/>
          <stop offset=".45" stop-color="var(--wall-mid)"/>
          <stop offset="1" stop-color="var(--wall-dark)"/>
        </linearGradient>
        <linearGradient id="gardenTone" x1="0" y1="0" x2="0" y2="1">
          <stop offset="0" stop-color="var(--garden-light)"/>
          <stop offset="1" stop-color="var(--garden-dark)"/>
        </linearGradient>
        <linearGradient id="houseTone" x1="0" y1="0" x2="0" y2="1">
          <stop offset="0" stop-color="var(--house-light)"/>
          <stop offset=".55" stop-color="var(--house-mid)"/>
          <stop offset="1" stop-color="var(--garden-dark)"/>
        </linearGradient>
      </defs>
      <rect class="collage__wall" width="668" height="945" fill="url(#wallTone)" role="img" aria-label="Photograph of a sandstone gallery wall hung with framed pictures"/>
      <circle class="collage__gate" cx="330" cy="760" r="445" fill="url(#gardenTone)" role="img" aria-label="Photograph of a timber gate with the Ashcombe Herbals Co sign among greenery"/>
      <circle class="collage__house" cx="610" cy="900" r="472" fill="url(#houseTone)" role="img" aria-label="Photograph of the two-storey sandstone lodge and its garden"/>
      <rect class="collage__tint" width="668" height="945" fill="#5a5040" opacity=".18"/>
    </svg>

    <svg class="poster__title" viewBox="0 0 668 945" aria-label="Thornfield Lodge 1852">
      <defs>
        <mask id="distress" maskUnits="userSpaceOnUse" x="0" y="0" width="668" height="945">
          <rect width="668" height="945" fill="#fff"/>
          <g fill="#000">
            <circle cx="345" cy="330" r="4"/><circle cx="350" cy="360" r="2.5"/><circle cx="342" cy="420" r="3"/>
            <circle cx="348" cy="470" r="5"/><circle cx="340" cy="488" r="2"/><circle cx="355" cy="300" r="2"/>
            <ellipse cx="418" cy="305" rx="6" ry="3"/><circle cx="430" cy="350" r="3"/><circle cx="424" cy="372" r="4"/>
            <circle cx="470" cy="330" r="2.5"/><circle cx="488" cy="410" r="3.5"/><circle cx="432" cy="455" r="2"/>
            <circle cx="496" cy="470" r="4"/><circle cx="460" cy="392" r="2"/><ellipse cx="505" cy="345" rx="3" ry="5"/>
            <circle cx="318" cy="585" r="3"/><circle cx="330" cy="640" r="4.5"/><circle cx="316" cy="700" r="2.5"/>
            <circle cx="360" cy="700" r="3"/><circle cx="372" cy="560" r="2"/><ellipse cx="340" cy="540" rx="5" ry="3"/>
            <circle cx="438" cy="560" r="3"/><circle cx="448" cy="620" r="4"/><circle cx="436" cy="690" r="2.5"/>
            <circle cx="505" cy="540" r="3.5"/><circle cx="512" cy="610" r="2"/><circle cx="498" cy="680" r="4"/>
            <circle cx="470" cy="520" r="2"/><circle cx="520" cy="705" r="2.5"/>
            <circle cx="262" cy="272" r="1.8"/><circle cx="258" cy="382" r="1.5"/><circle cx="266" cy="480" r="2"/>
            <circle cx="259" cy="640" r="1.6"/><circle cx="270" cy="735" r="1.8"/>
            <circle cx="262" cy="790" r="2.2"/><circle cx="305" cy="780" r="2.5"/><circle cx="352" cy="800" r="2"/>
            <circle cx="402" cy="785" r="2.6"/><circle cx="446" cy="805" r="1.8"/><circle cx="500" cy="792" r="2.4"/>
            <circle cx="530" cy="810" r="1.6"/><circle cx="324" cy="812" r="1.5"/>
          </g>
        </mask>
      </defs>
      <g mask="url(#distress)">
        <text class="title-numerals" x="322" y="501" font-size="300" textLength="191" lengthAdjust="spacingAndGlyphs">18</text>
        <text class="title-numerals" x="298" y="728" font-size="300" textLength="236" lengthAdjust="spacingAndGlyphs">52</text>
        <g class="title-slab" font-size="46" text-anchor="middle">
          <text x="263" y="302">T</text>
          <text x="263" y="352">H</text>
          <text x="263" y="402">O</text>
          <text x="263" y="452">R</text>
          <text x="263" y="502">N</text>
          <text x="263" y="552">F</text>
          <text x="263" y="602">I</text>
          <text x="263" y="652">E</text>
          <text x="263" y="702">L</text>
          <text x="263" y="752">D</text>
        </g>
        <text class="title-slab" x="245" y="820" font-size="74" textLength="299" lengthAdjust="spacingAndGlyphs">LODGE</text>
      </g>
    </svg>

    <p class="poster__caption">Built circa 1852 and subsequently residence of Police Magistrate<br>Major Edmund Harlow</p>
  </section>

  <div class="botanical" role="img" aria-label="Line illustration of a leafy botanical sprig"></div>
</main>
</body>
</html>
```